An A2 office artwork piece with quote overlay

I would like a piece of A2 office artwork, inspired by two things important to me and my business, overlaid with a quote. I have attached some photos and I have the quote I would like. My office is dark, minimalistic and modern in design (photo attached). I would like the artwork to contain some element of colour, but it should not be bright, the quote should be the main element with the photo and further design elements creating a subtle background.

The art will go on the wall behind my office chair and will appear in most of my online business video content, therefore I would like it to be inspiring.

The quote to be used:

"It is not because things are difficult that we do not dare; it is because we do not dare that they are difficult." - Tavrin

The property in the attached photograph is one we purchased recently and is an important milestone in my business.

I would also like an aviation reference to feature in the background as this was my career before I started my property business and I'm currently training to be a flying instructor. I have attached some aircraft photos which I have taken and I've attached some other items for inspiration. I am open to how the aviation reference is blended in.

Target Market(s)

This isn't a sales piece, it just needs to be intriguing.

Industry/Entity Type

Real estate

Font styles to use
Serif
Sans Serif
Script

Requirements
Must have
• Must have the building in the attached photograph and the quote.
Nice to have
• An aviation reference if this can be blended within the background.
Should not have
• Too many bright colours

```html
<!DOCTYPE html>
<html lang="en">
<head>
<meta charset="utf-8">
<title>Dare – Office Artwork</title>
<link rel="stylesheet" href="https://fonts.googleapis.com/css2?family=Jost:ital,wght@0,600;0,700;1,700&display=swap">
<style>
  :root {
    --gold-light: #f7efc0;
    --gold: #e2b94c;
    --gold-deep: #a87a2a;
    --ink: #05070a;
    --slate: #1d242c;
    --slate-dark: #10151b;
    --quote: #4a5563;
    --badge-text: #2a1608;
  }
  html, body {
    margin: 0;
    padding: 0;
    width: 849px;
    height: 1200px;
    overflow: hidden;
    background: #ffffff;
  }
  .artwork {
    display: block;
    width: 849px;
    height: 1200px;
  }
  .quote-line {
    font-family: "Jost", "Futura", sans-serif;
    font-weight: 700;
    fill: var(--quote);
  }
  .attribution {
    font-family: "Jost", "Futura", sans-serif;
    font-weight: 700;
    font-style: italic;
    fill: var(--badge-text);
  }
</style>
</head>
<body>
<svg class="artwork" viewBox="0 0 849 1200" xmlns="http://www.w3.org/2000/svg">
  <defs>
    <linearGradient id="goldFrame" x1="0" y1="0" x2="1" y2="1">
      <stop offset="0" stop-color="var(--gold)"/>
      <stop offset="0.3" stop-color="var(--gold-light)"/>
      <stop offset="0.6" stop-color="var(--gold-deep)"/>
      <stop offset="1" stop-color="var(--gold-light)"/>
    </linearGradient>
    <linearGradient id="goldEdge" x1="0" y1="0" x2="0" y2="1">
      <stop offset="0" stop-color="var(--gold)" stop-opacity="0"/>
      <stop offset="0.3" stop-color="var(--gold)"/>
      <stop offset="0.7" stop-color="var(--gold-light)"/>
      <stop offset="1" stop-color="var(--gold-deep)"/>
    </linearGradient>
    <linearGradient id="badgeGold" x1="0" y1="0" x2="1" y2="0">
      <stop offset="0" stop-color="#8a5a1c"/>
      <stop offset="0.45" stop-color="#f3d27a"/>
      <stop offset="0.75" stop-color="#c48f32"/>
      <stop offset="1" stop-color="#7a4d14"/>
    </linearGradient>
    <linearGradient id="leftShade" x1="0" y1="0" x2="1" y2="1">
      <stop offset="0" stop-color="#0b0f14"/>
      <stop offset="1" stop-color="#020304"/>
    </linearGradient>
    <linearGradient id="legShade" x1="0" y1="0" x2="1" y2="0">
      <stop offset="0" stop-color="var(--slate-dark)"/>
      <stop offset="1" stop-color="var(--slate)"/>
    </linearGradient>
    <linearGradient id="propertyTones" x1="0" y1="0" x2="0" y2="1">
      <stop offset="0" stop-color="#8fb5b4"/>
      <stop offset="0.15" stop-color="#6d4038"/>
      <stop offset="0.55" stop-color="#7a3a2c"/>
      <stop offset="0.8" stop-color="#3a2a26"/>
      <stop offset="1" stop-color="#1c1d20"/>
    </linearGradient>
    <linearGradient id="aircraftTones" x1="0" y1="0" x2="1" y2="1">
      <stop offset="0" stop-color="#6f86aa" stop-opacity="0.55"/>
      <stop offset="0.5" stop-color="#a89a86" stop-opacity="0.55"/>
      <stop offset="1" stop-color="#6f86aa" stop-opacity="0.45"/>
    </linearGradient>
    <clipPath id="leftPanel">
      <polygon points="20,20 455,20 110,1180 20,1180"/>
    </clipPath>
  </defs>

  <!-- frame -->
  <rect class="frame" x="0" y="0" width="849" height="1200" fill="url(#goldFrame)"/>
  <rect class="canvas-field" x="20" y="20" width="809" height="1160" fill="var(--ink)"/>

  <!-- banded left panel -->
  <g class="banded-panel" clip-path="url(#leftPanel)">
    <rect x="20" y="20" width="440" height="1160" fill="url(#leftShade)"/>
    <g fill="#1a2129" opacity="0.55">
      <rect x="20" y="34" width="440" height="16"/>
      <rect x="20" y="84" width="440" height="16"/>
      <rect x="20" y="134" width="440" height="16"/>
      <rect x="20" y="184" width="440" height="16"/>
      <rect x="20" y="234" width="440" height="16"/>
      <rect x="20" y="284" width="440" height="16"/>
      <rect x="20" y="334" width="440" height="16"/>
      <rect x="20" y="384" width="440" height="16"/>
      <rect x="20" y="434" width="440" height="16"/>
      <rect x="20" y="484" width="440" height="16"/>
      <rect x="20" y="534" width="440" height="16"/>
      <rect x="20" y="584" width="440" height="16"/>
    </g>
  </g>

  <!-- diagonal legs -->
  <polygon class="leg-left" points="455,21 350,392 345,418 120,1180 110,1180" fill="url(#legShade)"/>
  <polygon class="leg-left-shadow" points="455,21 110,1180 20,1180 20,700" fill="var(--slate-dark)" opacity="0.55"/>
  <polygon class="leg-right" points="350,392 826,1180 549,1180 345,418" fill="url(#legShade)"/>

  <!-- property photo area -->
  <polygon class="property-photo" role="img" aria-label="Photograph of a red-brick Victorian townhouse with lit bay windows at dusk, a dark car parked on the street below"
           points="345,418 549,1180 120,1180" fill="url(#propertyTones)"/>

  <!-- gold edges -->
  <line class="gold-edge" x1="455" y1="21" x2="110" y2="1180" stroke="url(#goldEdge)" stroke-width="2"/>
  <line class="gold-edge" x1="345" y1="418" x2="120" y2="1180" stroke="url(#goldEdge)" stroke-width="1.5"/>
  <line class="gold-edge" x1="350" y1="392" x2="826" y2="1180" stroke="url(#goldEdge)" stroke-width="2"/>

  <!-- aircraft illustration area -->
  <rect class="aircraft-illustration" role="img" aria-label="Illustration of a light training aircraft in flight, blue wings and tan fuselage"
        x="55" y="89" width="358" height="233" rx="6" fill="url(#aircraftTones)"/>

  <!-- quote -->
  <g class="quote" text-anchor="end">
    <text class="quote-line" x="818" y="89" font-size="74" textLength="353" lengthAdjust="spacingAndGlyphs">"IT IS NOT</text>
    <text class="quote-line" x="818" y="128" font-size="41" textLength="354" lengthAdjust="spacingAndGlyphs">BECAUSE THINGS</text>
    <text class="quote-line" x="818" y="175" font-size="52" textLength="390" lengthAdjust="spacingAndGlyphs">ARE DIFFICULT</text>
    <text class="quote-line" x="818" y="282" font-size="138" textLength="393" lengthAdjust="spacingAndGlyphs">THAT</text>
    <text class="quote-line" x="818" y="369" font-size="108" textLength="408" lengthAdjust="spacingAndGlyphs">WE DO</text>
    <text class="quote-line" x="818" y="429" font-size="67" textLength="402" lengthAdjust="spacingAndGlyphs">NOT DARE;</text>
    <text class="quote-line" x="818" y="486" font-size="52" textLength="381" lengthAdjust="spacingAndGlyphs">IT IS BECAUSE</text>
    <text class="quote-line" x="818" y="575" font-size="108" textLength="345" lengthAdjust="spacingAndGlyphs">WE DO</text>
    <text class="quote-line" x="818" y="633" font-size="67" textLength="316" lengthAdjust="spacingAndGlyphs">NOT DARE;</text>
    <text class="quote-line" x="818" y="682" font-size="52" textLength="272" lengthAdjust="spacingAndGlyphs">THAT THEY</text>
    <text class="quote-line" x="818" y="724" font-size="34" textLength="246" lengthAdjust="spacingAndGlyphs">ARE DIFFICULT."</text>
  </g>

  <!-- attribution badge -->
  <g class="attribution-badge">
    <rect x="650" y="749" width="156" height="47" fill="url(#badgeGold)"/>
    <text class="attribution" x="728" y="782" font-size="25" text-anchor="middle">- TAVRIN</text>
  </g>
</svg>
</body>
</html>
```